KeelDrift - Mobile App Design - Concept Only

We (KeelDrift) are looking for a new/better design for our mobile app. You can see and read more about our company and our current mobile app design on our website: www.keeldrift-demo.test. We would like an updated "concept" design for 3-4 screens - to include light/dark options (PNG or other file format is fine). 2-3 winners will be selected will be awarded the work for the entire app design (that will need to be completed in figma). You can view the current screenshots in the "Features" section of our website:

https://www.keeldrift-demo.test/#features
Updates

Target Market(s)

Marine / Boat Owner industry

Industry/Entity Type

Font styles to use
Other font styles liked:
• Inter

Colors
0054AA
0677BA
7BADD7
CADEEF
E8F1F8
00AB8E
00BBA5
67D7C9
C6EFE9
E9F9F6
FFF300
FFF600
FEFA6F
FFFEC7
FFFEE8
F0912C
F2A743
F7CA91
FBE8D2
FDF5EE
EB3D1F
EC4F4E
F09395
F8D3D4
FCEDEE
A7469A
B969AE
D3A5CF
EDDBEB
F8F0F9

Requirements
Must have
• (1) Must have 3-4 Pages from current App - from website (ex. "Dashboard", "Boat Details" Maintenance Logs") (2) Must accommodate a look and feel for both PHONE & TABLET concepts. (3) Must show Dark / Light Mode options.
Nice to have
• A better way to convey and organize a bunch of data about each boat/vessel. Brand Colors: Primary: #0478CC Secondary: #4AA6E8 Complimentary: #FD5C65, #FA884C, #F2B339, #13CE8B, #8D7EFB
Should not have
• Should not be a re-hash of existing design. We want a new look/feel.

```html
<!DOCTYPE html>
<html lang="en">
<head>
<meta charset="utf-8">
<title>KeelDrift – Mobile App Concept</title>
<link rel="stylesheet" href="https://fonts.googleapis.com/css2?family=Inter:wght@400;500;600;700&display=swap">
<style>
:root{
  --page:#e4ebf5;
  --heading:#1f2a3a;
  --brand:#0478CC;
  --brand-soft:#4AA6E8;
  --green:#13CE8B;
  --red:#FD5C65;
  --purple:#8D7EFB;
  --amber:#F2B339;
}
*{box-sizing:border-box;margin:0;padding:0}
html,body{width:766px;height:1200px;overflow:hidden}
body{background:var(--page);font-family:"Inter",sans-serif;position:relative;color:var(--heading)}
.mode-title{position:absolute;left:0;width:766px;text-align:center;font-size:26px;font-weight:700;letter-spacing:-.3px;color:var(--heading)}

.phone{
  --bg:#eef3f9;--surface:#fff;--header:#0478CC;--text:#1d2433;--muted:#7d8797;
  --line:#e3e8ef;--chip-line:#d5dbe5;--tag-bg:#eceff3;--tag-text:#8a93a1;
  --ok-bg:#dcf6ec;--ok:#12b67d;--bad-bg:#fde4e5;--bad:#f2505a;--nav:#fff;--seg:#fff;
  position:absolute;width:370px;height:800px;border-radius:30px;overflow:hidden;
  background:var(--bg);transform:scale(.511);transform-origin:0 0;color:var(--text);
}
.phone.dark{
  --bg:#15112a;--surface:#211c3b;--header:#231e40;--text:#f3f3f8;--muted:#8f8cab;
  --line:#383259;--chip-line:#3d3862;--tag-bg:#37325b;--tag-text:#a8a5c4;
  --ok-bg:#164a3b;--ok:#2fe0a0;--bad-bg:#4b1f34;--bad:#ff6b74;--nav:#221d3e;--seg:#221d3e;
}
svg.ic{width:18px;height:18px;fill:none;stroke:currentColor;stroke-width:1.8;stroke-linecap:round;stroke-linejoin:round;flex:none}

.app-bar{position:absolute;top:0;left:0;right:0;height:105px;background:var(--header);color:#fff}
.status{position:absolute;top:14px;left:45px;right:28px;display:flex;justify-content:space-between;align-items:center;font-size:16px;font-weight:600}
.status svg{width:74px;height:14px}
.bar-row{position:absolute;top:58px;left:18px;right:18px;height:36px;display:flex;align-items:center;justify-content:space-between}
.bar-title{font-size:18px;font-weight:700}
.brand{display:flex;align-items:center;gap:7px;font-size:19px;font-weight:700;letter-spacing:.2px}
.brand-dot{width:20px;height:20px;border-radius:50%;background:#fff}
.bell{position:relative;width:22px;height:22px}
.bell svg{width:22px;height:22px}
.bell::after{content:"";position:absolute;top:0;right:0;width:7px;height:7px;border-radius:50%;background:var(--red)}
.bar-side{width:22px}
.bar-row svg.back{width:22px;height:22px}

.screen{position:absolute;top:105px;left:0;right:0;bottom:0;padding:0 15px;overflow:hidden}
.screen.with-nav{bottom:78px}

/* My Yacht */
.screen-title{font-size:17px;font-weight:700;margin-top:24px}
.chips{display:flex;gap:9px;margin-top:14px;white-space:nowrap}
.chip{height:31px;padding:0 18px;border:1px solid var(--chip-line);border-radius:6px;font-size:13px;font-weight:500;color:var(--muted);display:flex;align-items:center;flex:none}
.chip.on{background:var(--brand);border-color:var(--brand);color:#fff}
.sort{display:flex;justify-content:flex-end;align-items:center;gap:5px;font-size:11px;color:var(--muted);margin:13px 3px 12px}
.sort b{color:var(--text);font-weight:600}
.sort svg{width:13px;height:13px}
.yacht-card{background:var(--surface);border-radius:10px;padding:17px 18px 0;margin-bottom:9px}
.yacht-head{display:flex;gap:12px;height:73px}
.avatar{width:40px;height:40px;border-radius:50%;display:flex;align-items:center;justify-content:center;font-weight:700;font-size:16px;flex:none}
.av-purple{background:var(--purple);color:#fff}
.av-amber{background:var(--amber);color:#fff}
.av-gray{background:#8d93a0;color:#fff}
.yacht-name{font-size:13px;font-weight:600;margin-top:1px}
.meta{font-size:10.5px;color:var(--muted);margin-top:4px;display:flex;align-items:center;gap:3px;white-space:nowrap}
.meta svg{width:12px;height:12px}
.yacht-foot{border-top:1px solid var(--line);height:68px;display:flex;align-items:center;justify-content:space-between}
.tag{font-size:10.5px;font-weight:600;padding:4px 7px;border-radius:3px;background:var(--tag-bg);color:var(--tag-text);letter-spacing:.3px}
.tag.ok{background:var(--ok-bg);color:var(--ok)}
.tag.bad{background:var(--bad-bg);color:var(--bad)}
.actions{display:flex;gap:8px}
.btn{height:32px;width:84px;border-radius:5px;font-size:13px;font-weight:500;display:flex;align-items:center;justify-content:center}
.btn.primary{background:var(--brand);color:#fff}
.btn.danger{border:1px solid var(--bad);color:var(--bad)}
.link{color:var(--brand);font-size:13px;font-weight:600;display:flex;align-items:center;gap:6px}
.dark .link{color:#3f9be0}
.link svg{width:14px;height:14px;stroke-width:2.2}
.fab{position:absolute;left:307px;top:654px;width:46px;height:46px;border-radius:50%;background:var(--brand);color:#fff;display:flex;align-items:center;justify-content:center;box-shadow:0 4px 10px rgba(4,120,204,.3)}
.fab svg{width:22px;height:22px;stroke-width:2}
.tabbar{position:absolute;left:0;right:0;bottom:0;height:78px;background:var(--nav);display:flex;justify-content:space-around;padding-top:12px}
.tab{display:flex;flex-direction:column;align-items:center;gap:5px;font-size:11px;font-weight:500;color:var(--muted);width:80px}
.tab svg{width:22px;height:22px}
.tab.on{color:var(--brand)}

/* Boat Details */
.segment{margin-top:15px;height:40px;background:var(--seg);border-radius:10px;display:flex;align-items:center;padding:0 5px}
.seg{flex:1;height:31px;border-radius:16px;display:flex;align-items:center;justify-content:center;font-size:13px;font-weight:500;color:var(--muted)}
.seg.on{background:var(--brand);color:#fff}
.stepper{margin-top:8px;height:57px;background:var(--surface);border-radius:10px;position:relative;display:flex;padding:0 2px}
.stepper::before{content:"";position:absolute;left:52px;right:42px;top:18px;height:1px;background:var(--chip-line)}
.step{flex:1;display:flex;flex-direction:column;align-items:center;font-size:11px;color:var(--muted);position:relative}
.step i{width:7px;height:7px;border-radius:50%;background:var(--muted);margin:15px 0 8px}
.step.on{color:var(--brand)}
.step.on i{background:var(--brand)}
.panel{margin-top:8px;background:var(--surface);border-radius:10px;padding:15px}
.ident{display:flex;align-items:center;gap:12px}
.ident .avatar{width:56px;height:56px;font-size:17px}
.ident h3{font-size:17px;font-weight:700}
.row{height:41px;border:1px solid var(--line);border-radius:6px;display:flex;align-items:center;gap:9px;padding:0 10px 0 11px;font-size:11.5px;font-weight:600;margin-top:8px}
.row svg{width:19px;height:19px;color:var(--brand)}
.row .val{margin-left:auto;font-weight:400;color:var(--muted);display:flex;align-items:center;gap:5px}
.ident + .row{margin-top:15px}
.panel h4{font-size:15px;font-weight:700;margin:8px 0 15px}
.dot-ok{width:6px;height:6px;border-radius:50%;background:var(--green)}
.flag{width:28px;height:14px}

/* Maintenance */
.log{background:var(--surface);border-radius:10px;padding:18px 18px 0;margin-top:15px}
.log + .log{margin-top:8px}
.log-head{display:flex;gap:12px;height:93px}
.log-icon{width:40px;height:40px;border-radius:50%;background:var(--brand);color:#fff;display:flex;align-items:center;justify-content:center;flex:none}
.log-icon svg{width:20px;height:20px}
.log-icon svg.solid{fill:#fff;stroke:none}
.log-title{font-size:13px;font-weight:600;margin-top:1px}
.log .meta{margin-top:6px}
.log-foot{border-top:1px solid var(--line);height:60px;display:flex;align-items:center;justify-content:space-between}
</style>
</head>
<body>
<svg width="0" height="0" style="position:absolute">
  <defs>
    <symbol id="i-bell" viewBox="0 0 24 24"><path d="M6 16v-5a6 6 0 0 1 12 0v5l1.5 2h-15z M10 20.5a2 2 0 0 0 4 0"/></symbol>
    <symbol id="i-back" viewBox="0 0 24 24"><path d="M19 12H5 M11 6l-6 6 6 6"/></symbol>
    <symbol id="i-chev" viewBox="0 0 24 24"><path d="M9 5l7 7-7 7"/></symbol>
    <symbol id="i-pin" viewBox="0 0 24 24"><path d="M12 21s-6.5-6-6.5-11a6.5 6.5 0 0 1 13 0c0 5-6.5 11-6.5 11z"/><circle cx="12" cy="10" r="2.2"/></symbol>
    <symbol id="i-share" viewBox="0 0 24 24"><circle cx="18" cy="5" r="2.5"/><circle cx="6" cy="12" r="2.5"/><circle cx="18" cy="19" r="2.5"/><path d="M8.2 10.8l7.6-4.5 M8.2 13.2l7.6 4.5"/></symbol>
    <symbol id="i-ship" viewBox="0 0 24 24"><path d="M3.5 15l2.5 5h12l2.5-5-8.5-3z M7 13V8h10v5 M10 8V4.5h4V8 M3 21.5h18"/></symbol>
    <symbol id="i-hash" viewBox="0 0 24 24"><rect x="3" y="5.5" width="18" height="13" rx="2"/><path d="M7.5 10v4.5 M10.5 10h2.5v2.2h-2.5v2.3H13 M16 10h2v4.5h-2"/></symbol>
    <symbol id="i-cal" viewBox="0 0 24 24"><rect x="4" y="5" width="16" height="15" rx="2"/><path d="M4 10h16 M8 3v4 M16 3v4 M8 14h1 M12 14h1 M16 14h0.5 M8 17h1 M12 17h1"/></symbol>
    <symbol id="i-brand" viewBox="0 0 24 24"><rect x="3" y="6" width="18" height="12" rx="6"/><path d="M10 9.5v5h2.2a1.3 1.3 0 0 0 0-2.5H10 M10 9.5h2a1.2 1.2 0 0 1 0 2.5"/></symbol>
    <symbol id="i-model" viewBox="0 0 24 24"><rect x="3" y="6" width="18" height="12" rx="6"/><path d="M8.5 14.5v-5l3.5 3 3.5-3v5"/></symbol>
    <symbol id="i-flag" viewBox="0 0 24 24"><path d="M5 21V4 M5 4h13l-2.5 4.5L18 13H5"/></symbol>
    <symbol id="i-info" viewBox="0 0 24 24"><circle cx="12" cy="12" r="9"/><path d="M12 11v5.5 M12 7.8v.4"/></symbol>
    <symbol id="i-sound" viewBox="0 0 24 24"><path d="M4 9.5h3.5L12 5.5v13l-4.5-4H4z M15.5 9a4 4 0 0 1 0 6 M18 6.5a7.5 7.5 0 0 1 0 11"/></symbol>
    <symbol id="i-fan" viewBox="0 0 24 24"><rect x="4" y="4" width="16" height="16" rx="3"/><circle cx="12" cy="12" r="4.2"/><circle cx="12" cy="12" r="1"/></symbol>
    <symbol id="i-plug" viewBox="0 0 24 24"><path d="M9 3v4 M15 3v4 M7 7h10v4a5 5 0 0 1-10 0z M12 16v5"/></symbol>
    <symbol id="i-bolt" viewBox="0 0 24 24"><path d="M13.5 2.5L5 14h6l-1 7.5L19 10h-6.2z"/></symbol>
    <symbol id="i-gear" viewBox="0 0 24 24"><circle cx="12" cy="12" r="3.2"/><path d="M12 3v2.5 M12 18.5V21 M3 12h2.5 M18.5 12H21 M5.6 5.6l1.8 1.8 M16.6 16.6l1.8 1.8 M5.6 18.4l1.8-1.8 M16.6 7.4l1.8-1.8"/><circle cx="12" cy="12" r="6.5"/></symbol>
    <symbol id="i-doc" viewBox="0 0 24 24"><path d="M6 3h8l4 4v14H6z M14 3v4h4 M9 14l2 2 4-4"/></symbol>
    <symbol id="i-user" viewBox="0 0 24 24"><circle cx="12" cy="12" r="9"/><circle cx="12" cy="10" r="3"/><path d="M6.5 18.2a6.5 6.5 0 0 1 11 0"/></symbol>
    <symbol id="i-sort" viewBox="0 0 24 24"><path d="M4 7h16 M7 12h10 M10 17h4"/></symbol>
    <symbol id="i-down" viewBox="0 0 24 24"><path d="M6 9l6 6 6-6"/></symbol>
    <symbol id="i-plus" viewBox="0 0 24 24"><path d="M12 5v14 M5 12h14"/></symbol>
    <symbol id="i-status" viewBox="0 0 74 14"><g fill="#fff" stroke="none"><rect x="0" y="9" width="3" height="4" rx="1"/><rect x="5" y="6.5" width="3" height="6.5" rx="1"/><rect x="10" y="4" width="3" height="9" rx="1"/><rect x="15" y="1.5" width="3" height="11.5" rx="1"/><path d="M33 13l-2.6-3a3.8 3.8 0 0 1 5.2 0z"/><rect x="49" y="2" width="20" height="10" rx="3" fill="none" stroke="#fff" stroke-opacity=".5"/><rect x="51" y="4" width="16" height="6" rx="1.5"/><rect x="70" y="5.5" width="1.6" height="3.2" rx=".8" fill-opacity=".5"/></g><path d="M26 6.5a10 10 0 0 1 14 0 M28.5 9a6 6 0 0 1 9 0" stroke="#fff" stroke-width="2" fill="none" stroke-linecap="round"/></symbol>
    <symbol id="i-us" viewBox="0 0 28 14"><rect width="28" height="14" fill="#fff"/><g fill="#d8323c"><rect y="0" width="28" height="1.1"/><rect y="2.15" width="28" height="1.1"/><rect y="4.3" width="28" height="1.1"/><rect y="6.45" width="28" height="1.1"/><rect y="8.6" width="28" height="1.1"/><rect y="10.75" width="28" height="1.1"/><rect y="12.9" width="28" height="1.1"/></g><rect width="12" height="7.5" fill="#2e3f8f"/></symbol>
  </defs>
</svg>

<h1 class="mode-title" style="top:44px">Light Mode</h1>
<h1 class="mode-title" style="top:636px">Dark Mode</h1>

<!-- ========== LIGHT ========== -->
<div class="phone" style="left:59px;top:118px">
  <header class="app-bar">
    <div class="status">9:41<svg><use href="#i-status"/></svg></div>
    <div class="bar-row"><span class="bar-side"></span><span class="brand"><i class="brand-dot"></i>KeelDrift</span><span class="bell"><svg class="ic"><use href="#i-bell"/></svg></span></div>
  </header>
  <main class="screen with-nav">
    <h2 class="screen-title">My Yacht</h2>
    <div class="chips"><span class="chip on">All</span><span class="chip">Invite</span><span class="chip">In Service</span><span class="chip">Hauled</span><span class="chip">Archived</span></div>
    <div class="sort"><svg class="ic"><use href="#i-sort"/></svg>Sort by <b>Newest</b><svg class="ic"><use href="#i-down"/></svg></div>
    <article class="yacht-card">
      <div class="yacht-head"><span class="avatar av-purple">O</span><div><div class="yacht-name">Ohana</div><div class="meta">2015 · Presto · 500 Fly</div><div class="meta"><svg class="ic"><use href="#i-pin"/></svg>Sarasota, FL</div></div></div>
      <div class="yacht-foot"><span class="tag">INVITE</span><div class="actions"><span class="btn primary">Accept</span><span class="btn danger">Reject</span></div></div>
    </article>
    <article class="yacht-card">
      <div class="yacht-head"><span class="avatar av-amber">ES</span><div><div class="yacht-name">Endless Summer</div><div class="meta">2012 · Rivale · 46SC</div><div class="meta"><svg class="ic"><use href="#i-pin"/></svg>Miami, FL</div></div></div>
      <div class="yacht-foot"><span class="tag ok">IN SERVICE</span><span class="link">See Details<svg class="ic"><use href="#i-chev"/></svg></span></div>
    </article>
    <article class="yacht-card">
      <div class="yacht-head"><span class="avatar av-gray">S</span><div><div class="yacht-name">Serenity</div><div class="meta">2020 · Ocean Alder · 70</div><div class="meta"><svg class="ic"><use href="#i-pin"/></svg>Ft Lauderdale, FL</div></div></div>
      <div class="yacht-foot"><span class="tag bad">IN SERVICE</span><span class="link">See Details<svg class="ic"><use href="#i-chev"/></svg></span></div>
    </article>
  </main>
  <span class="fab"><svg class="ic"><use href="#i-plus"/></svg></span>
  <nav class="tabbar">
    <span class="tab on"><svg class="ic"><use href="#i-ship"/></svg>My Yacht</span>
    <span class="tab"><svg class="ic"><use href="#i-doc"/></svg>My Task</span>
    <span class="tab"><svg class="ic"><use href="#i-user"/></svg>Account</span>
  </nav>
</div>

<div class="phone" style="left:289px;top:154px">
  <header class="app-bar">
    <div class="status">9:41<svg><use href="#i-status"/></svg></div>
    <div class="bar-row"><svg class="ic back"><use href="#i-back"/></svg><span class="bar-title">Boat Details</span><span class="bell"><svg class="ic"><use href="#i-bell"/></svg></span></div>
  </header>
  <main class="screen">
    <div class="segment"><span class="seg on">Details</span><span class="seg">Engines</span><span class="seg">Other</span></div>
    <div class="stepper"><span class="step on"><i></i>General</span><span class="step"><i></i>Dimensions</span><span class="step"><i></i>Electrical</span><span class="step"><i></i>Structural</span></div>
    <section class="panel">
      <div class="ident"><span class="avatar av-purple">CD</span><h3>Carpe Diem</h3></div>
      <div class="row"><svg class="ic"><use href="#i-share"/></svg>Shares<span class="val">4 <svg class="ic" style="width:16px;height:16px"><use href="#i-chev"/></svg></span></div>
    </section>
    <section class="panel">
      <h4>General</h4>
      <div class="row"><svg class="ic"><use href="#i-ship"/></svg>Type<span class="val">Motor Vessel</span></div>
      <div class="row"><svg class="ic"><use href="#i-hash"/></svg>HIN<span class="val">US-SERT5100C317</span></div>
      <div class="row"><svg class="ic"><use href="#i-cal"/></svg>Year<span class="val">2018</span></div>
      <div class="row"><svg class="ic"><use href="#i-brand"/></svg>Brand<span class="val">L Class</span></div>
      <div class="row"><svg class="ic"><use href="#i-model"/></svg>Model<span class="val">L590</span></div>
      <div class="row"><svg class="ic"><use href="#i-flag"/></svg>Flag<span class="val"><svg class="flag"><use href="#i-us"/></svg>United States</span></div>
      <div class="row"><svg class="ic"><use href="#i-info"/></svg>Status<span class="val"><i class="dot-ok"></i>In Service</span></div>
    </section>
  </main>
</div>

<div class="phone" style="left:518px;top:118px">
  <header class="app-bar">
    <div class="status">9:41<svg><use href="#i-status"/></svg></div>
    <div class="bar-row"><svg class="ic back"><use href="#i-back"/></svg><span class="bar-title">Maintenance Logs</span><span class="bell"><svg class="ic"><use href="#i-bell"/></svg></span></div>
  </header>
  <main class="screen">
    <article class="log">
      <div class="log-head"><span class="log-icon"><svg class="ic"><use href="#i-sound"/></svg></span><div><div class="log-title">Audio/Visual</div><div class="meta"><svg class="ic"><use href="#i-cal"/></svg>08/18/2021</div><div class="meta"><svg class="ic"><use href="#i-gear"/></svg>Update Firmware (Salon)</div><div class="meta"><svg class="ic"><use href="#i-gear"/></svg>3 hrs</div></div></div>
      <div class="log-foot"><span class="tag">STARBOARD</span><span class="link">See Details<svg class="ic"><use href="#i-chev"/></svg></span></div>
    </article>
    <article class="log">
      <div class="log-head"><span class="log-icon"><svg class="ic"><use href="#i-fan"/></svg></span><div><div class="log-title">HVAC</div><div class="meta"><svg class="ic"><use href="#i-cal"/></svg>07/01/2022</div><div class="meta"><svg class="ic"><use href="#i-gear"/></svg>Cleaned Strainer</div><div class="meta"><svg class="ic"><use href="#i-gear"/></svg>N/A</div></div></div>
      <div class="log-foot"><span class="tag">PORT 1</span><span class="link">See Details<svg class="ic"><use href="#i-chev"/></svg></span></div>
    </article>
    <article class="log">
      <div class="log-head"><span class="log-icon"><svg class="ic"><use href="#i-plug"/></svg></span><div><div class="log-title">Electronics</div><div class="meta"><svg class="ic"><use href="#i-cal"/></svg>06/06/2022</div><div class="meta"><svg class="ic"><use href="#i-gear"/></svg>Replaced Chartplotter</div><div class="meta"><svg class="ic"><use href="#i-gear"/></svg>N/A</div></div></div>
      <div class="log-foot"><span class="tag">CENTER</span><span class="link">See Details<svg class="ic"><use href="#i-chev"/></svg></span></div>
    </article>
    <article class="log">
      <div class="log-head"><span class="log-icon"><svg class="ic solid"><use href="#i-bolt"/></svg></span><div><div class="log-title">Generator</div><div class="meta"><svg class="ic"><use href="#i-cal"/></svg>05/01/2022</div><div class="meta"><svg class="ic"><use href="#i-gear"/></svg>Changed Oil, Filters and Anode</div><div class="meta"><svg class="ic"><use href="#i-gear"/></svg>950 hrs</div></div></div>
      <div class="log-foot"><span class="tag">CENTER</span><span class="link">See Details<svg class="ic"><use href="#i-chev"/></svg></span></div>
    </article>
  </main>
</div>

<!-- ========== DARK ========== -->
<div class="phone dark" style="left:59px;top:710px">
  <header class="app-bar">
    <div class="status">9:41<svg><use href="#i-status"/></svg></div>
    <div class="bar-row"><span class="bar-side"></span><span class="brand"><i class="brand-dot"></i>KeelDrift</span><span class="bell"><svg class="ic"><use href="#i-bell"/></svg></span></div>
  </header>
  <main class="screen with-nav">
    <h2 class="screen-title">My Yacht</h2>
    <div class="chips"><span class="chip on">All</span><span class="chip">Invite</span><span class="chip">In Service</span><span class="chip">Hauled</span><span class="chip">Archived</span></div>
    <div class="sort"><svg class="ic"><use href="#i-sort"/></svg>Sort by <b>Newest</b><svg class="ic"><use href="#i-down"/></svg></div>
    <article class="yacht-card">
      <div class="yacht-head"><span class="avatar av-purple">O</span><div><div class="yacht-name">Ohana</div><div class="meta">2015 · Presto · 500 Fly</div><div class="meta"><svg class="ic"><use href="#i-pin"/></svg>Sarasota, FL</div></div></div>
      <div class="yacht-foot"><span class="tag">INVITE</span><div class="actions"><span class="btn primary">Accept</span><span class="btn danger">Reject</span></div></div>
    </article>
    <article class="yacht-card">
      <div class="yacht-head"><span class="avatar av-amber">ES</span><div><div class="yacht-name">Endless Summer</div><div class="meta">2012 · Rivale · 46SC</div><div class="meta"><svg class="ic"><use href="#i-pin"/></svg>Miami, FL</div></div></div>
      <div class="yacht-foot"><span class="tag ok">IN SERVICE</span><span class="link">See Details<svg class="ic"><use href="#i-chev"/></svg></span></div>
    </article>
    <article class="yacht-card">
      <div class="yacht-head"><span class="avatar av-gray">S</span><div><div class="yacht-name">Serenity</div><div class="meta">2020 · Ocean Alder · 70</div><div class="meta"><svg class="ic"><use href="#i-pin"/></svg>Ft Lauderdale, FL</div></div></div>
      <div class="yacht-foot"><span class="tag bad">IN SERVICE</span><span class="link">See Details<svg class="ic"><use href="#i-chev"/></svg></span></div>
    </article>
  </main>
  <span class="fab"><svg class="ic"><use href="#i-plus"/></svg></span>
  <nav class="tabbar">
    <span class="tab on"><svg class="ic"><use href="#i-ship"/></svg>My Yacht</span>
    <span class="tab"><svg class="ic"><use href="#i-doc"/></svg>My Task</span>
    <span class="tab"><svg class="ic"><use href="#i-user"/></svg>Account</span>
  </nav>
</div>

<div class="phone dark" style="left:289px;top:746px">
  <header class="app-bar">
    <div class="status">9:41<svg><use href="#i-status"/></svg></div>
    <div class="bar-row"><svg class="ic back"><use href="#i-back"/></svg><span class="bar-title">Boat Details</span><span class="bell"><svg class="ic"><use href="#i-bell"/></svg></span></div>
  </header>
  <main class="screen">
    <div class="segment"><span class="seg on">Details</span><span class="seg">Engines</span><span class="seg">Other</span></div>
    <div class="stepper"><span class="step on"><i></i>General</span><span class="step"><i></i>Dimensions</span><span class="step"><i></i>Electrical</span><span class="step"><i></i>Structural</span></div>
    <section class="panel">
      <div class="ident"><span class="avatar av-purple">CD</span><h3>Carpe Diem</h3></div>
      <div class="row"><svg class="ic"><use href="#i-share"/></svg>Shares<span class="val">4 <svg class="ic" style="width:16px;height:16px"><use href="#i-chev"/></svg></span></div>
    </section>
    <section class="panel">
      <h4>General</h4>
      <div class="row"><svg class="ic"><use href="#i-ship"/></svg>Type<span class="val">Motor Vessel</span></div>
      <div class="row"><svg class="ic"><use href="#i-hash"/></svg>HIN<span class="val">US-SERT5100C317</span></div>
      <div class="row"><svg class="ic"><use href="#i-cal"/></svg>Year<span class="val">2018</span></div>
      <div class="row"><svg class="ic"><use href="#i-brand"/></svg>Brand<span class="val">L Class</span></div>
      <div class="row"><svg class="ic"><use href="#i-model"/></svg>Model<span class="val">L590</span></div>
      <div class="row"><svg class="ic"><use href="#i-flag"/></svg>Flag<span class="val"><svg class="flag"><use href="#i-us"/></svg>United States</span></div>
      <div class="row"><svg class="ic"><use href="#i-info"/></svg>Status<span class="val"><i class="dot-ok"></i>In Service</span></div>
    </section>
  </main>
</div>

<div class="phone dark" style="left:518px;top:710px">
  <header class="app-bar">
    <div class="status">9:41<svg><use href="#i-status"/></svg></div>
    <div class="bar-row"><svg class="ic back"><use href="#i-back"/></svg><span class="bar-title">Maintenance Logs</span><span class="bell"><svg class="ic"><use href="#i-bell"/></svg></span></div>
  </header>
  <main class="screen">
    <article class="log">
      <div class="log-head"><span class="log-icon"><svg class="ic"><use href="#i-sound"/></svg></span><div><div class="log-title">Audio/Visual</div><div class="meta"><svg class="ic"><use href="#i-cal"/></svg>08/18/2021</div><div class="meta"><svg class="ic"><use href="#i-gear"/></svg>Update Firmware (Salon)</div><div class="meta"><svg class="ic"><use href="#i-gear"/></svg>3 hrs</div></div></div>
      <div class="log-foot"><span class="tag">STARBOARD</span><span class="link">See Details<svg class="ic"><use href="#i-chev"/></svg></span></div>
    </article>
    <article class="log">
      <div class="log-head"><span class="log-icon"><svg class="ic"><use href="#i-fan"/></svg></span><div><div class="log-title">HVAC</div><div class="meta"><svg class="ic"><use href="#i-cal"/></svg>07/01/2022</div><div class="meta"><svg class="ic"><use href="#i-gear"/></svg>Cleaned Strainer</div><div class="meta"><svg class="ic"><use href="#i-gear"/></svg>N/A</div></div></div>
      <div class="log-foot"><span class="tag">PORT 1</span><span class="link">See Details<svg class="ic"><use href="#i-chev"/></svg></span></div>
    </article>
    <article class="log">
      <div class="log-head"><span class="log-icon"><svg class="ic"><use href="#i-plug"/></svg></span><div><div class="log-title">Electronics</div><div class="meta"><svg class="ic"><use href="#i-cal"/></svg>06/06/2022</div><div class="meta"><svg class="ic"><use href="#i-gear"/></svg>Replaced Chartplotter</div><div class="meta"><svg class="ic"><use href="#i-gear"/></svg>N/A</div></div></div>
      <div class="log-foot"><span class="tag">CENTER</span><span class="link">See Details<svg class="ic"><use href="#i-chev"/></svg></span></div>
    </article>
    <article class="log">
      <div class="log-head"><span class="log-icon"><svg class="ic solid"><use href="#i-bolt"/></svg></span><div><div class="log-title">Generator</div><div class="meta"><svg class="ic"><use href="#i-cal"/></svg>05/01/2022</div><div class="meta"><svg class="ic"><use href="#i-gear"/></svg>Changed Oil, Filters and Anode</div><div class="meta"><svg class="ic"><use href="#i-gear"/></svg>950 hrs</div></div></div>
      <div class="log-foot"><span class="tag">CENTER</span><span class="link">See Details<svg class="ic"><use href="#i-chev"/></svg></span></div>
    </article>
  </main>
</div>
</body>
</html>
```